Book Cover Design Project - SIMPLE ART, Pre-Concepted

We already have a full design concept for the cover art. It is however in a low quality word document format. This project is to recreate existing example guideline art in as much vector art possible for great quality print production. Artistic flare is welcome. This will be for a book cover (front/back) and I want the quality to be excellent.

Art to be provided in Adobe Illustrator format. The book will be 6wide x 9high, so the artboard for the cover needs to be set up to 12.5 wide x 9 high with .125" bleeds.

Copy content for the spine: "Beneath a Copper Evening Sky Still" RL Moskowicz.

Here is a link to download the word document "template" and a new photo for the back page. I'm not sure that I like the new photo, it is possible the old one in the word document will work.

www.bluemarlinpressworks.com/uploads/QuillHavenSharedFiles.zip

I've got a fast deadline on this project because the client would like to have manufacturing completed by Christmas...which is why this is only a 2 day project. I appreciate your interest in our project.

Gordon

Try this link...seems I was missing the .zip extension which may have been causing problems.

Requirements
Must have
• Adobe Illustrator Files
CMYK color setup - no color definitions for project
Artboard Size: 12.625 wide x 9.125 high
Art Orientation: Flat image should have the back book page on the left side, front page on the right side, spine copy running down the middle.

```html
<!DOCTYPE html>
<html lang="en">
<head>
<meta charset="utf-8">
<title>Beneath a Copper Evening Sky Still — Cover</title>
<link href="https://fonts.googleapis.com/css2?family=Oswald:wght@600;700&family=Ubuntu:wght@300;400;500&display=swap" rel="stylesheet">
<style>
  :root {
    --paper: #ffffff;
    --oxblood: #5b1a10;
    --ink-title: #5a1810;
    --parchment: #e9d7a6;
    --parchment-dark: #b98f55;
    --wood: #6b2f17;
    --wood-light: #9a4c27;
    --white: #ffffff;
    --photo-tone: #8f6f5c;
    --title-font: "Oswald", "Arial Narrow", sans-serif;
    --body-font: "Ubuntu", "Helvetica", sans-serif;
  }
  * { margin: 0; padding: 0; box-sizing: border-box; }
  html, body { width: 1200px; height: 887px; overflow: hidden; background: var(--paper); }

  .cover {
    position: absolute; left: 30px; top: 30px;
    width: 1140px; height: 827px;
    background: var(--oxblood);
  }

  /* Back panel */
  .back-cover { position: absolute; left: 0; top: 0; width: 548px; height: 827px; }
  .back-cover__heading {
    position: absolute; left: 0; top: 54px; width: 548px;
    text-align: center; color: var(--white);
    font: 400 19px/1 var(--body-font);
  }
  .back-cover__bio {
    position: absolute; left: 138px; top: 84px; width: 362px;
    color: var(--white); text-align: justify;
    font: 300 10.2px/13.2px var(--body-font);
  }
  .author-portrait {
    position: absolute; left: 135px; top: 598px; width: 313px; height: 229px;
    background: radial-gradient(ellipse at 50% 35%, #b89a86 0%, var(--photo-tone) 40%, #3d3530 75%, #2b2622 100%);
    border-radius: 140px 140px 0 0;
  }

  /* Front panel */
  .front-cover {
    position: absolute; left: 548px; top: 0; width: 592px; height: 755px;
    background: radial-gradient(circle at 55% 42%, #fbf3dc 0%, var(--parchment) 35%, #d2b47c 70%, var(--parchment-dark) 100%);
    overflow: hidden;
  }
  .front-cover__cross-image {
    position: absolute; left: 150px; top: 142px; width: 328px; height: 528px;
    background: radial-gradient(ellipse at 50% 45%, rgba(154,76,39,.45) 0%, rgba(107,47,23,.28) 45%, rgba(107,47,23,0) 75%);
  }

  .title-word {
    position: absolute; color: var(--ink-title);
    font: 700 50px/1 var(--title-font); letter-spacing: .5px; white-space: nowrap;
  }
  .title-word--top { left: 122px; top: 64px; }
  .title-word--left { left: 163px; top: 220px; }
  .title-word--right { left: 392px; top: 340px; }
  .title-word--bottom { left: 256px; top: 679px; }

  .spine-title, .spine-author {
    position: absolute; writing-mode: vertical-rl; white-space: nowrap;
  }
  .spine-title {
    left: 11px; top: 222px; color: var(--ink-title);
    font: 700 19px/1 var(--title-font); letter-spacing: .5px;
  }
  .spine-author {
    left: 12px; top: 634px; color: var(--white);
    font: 400 19px/1 var(--body-font);
  }

  .front-cover__tagline {
    position: absolute; left: 548px; top: 772px; width: 592px;
    text-align: center; color: var(--white);
    font: 300 21px/1 var(--body-font);
  }
  .front-cover__tagline strong { font-weight: 500; }
</style>
</head>
<body>
  <main class="cover">
    <section class="back-cover">
      <h2 class="back-cover__heading">About the author</h2>
      <p class="back-cover__bio">The word of God says that “I know the plans I have for you” (Jeremiah 29:11) and that “before I formed you in the womb I knew you” (Jeremiah 1:15). These verses of scripture depict the life of Raymond L Moskowicz. As a little boy Raymond was always told that he was going to be a preacher. The magnitude of this repeated statement and exactly what it entailed was not taken seriously or truly understood, at that time. It was not Raymond’s plan or desire to be a preacher, and he tried to do anything and everything to avoid the talks of him becoming one. Raymond’s path of life, although he believed in God, took him down the road that led him away from God. His struggles with life’s events and being an introvert kept him emotionally troubled, in a state of depression and wanting to commit suicide. Yet, as the Lord was with Jeremiah, even so was the Lord with Raymond. The Lord was to show Raymond just what it meant to have complete trust in Him and to know that He would always provide a way of an escape. Before Raymond came to the point of carrying out his plans to commit suicide, he prayed a simple prayer that God would give him a new family. At that exact moment Raymond’s life began to take a new direction. He began to seek after the Lord; it became his quest to find out what it meant to be a servant of God. Because of his being an introvert, he began to write his emotions on paper in the form of poems. Those poems gave him the strength to come out of depression and began his two year journey to find God. Raymond’s relationship with Jesus and salvation journey began at the age of nineteen. The poetry writing started as a therapeutic remedy for his troubled past, but developed into the psalms of Raymond because of God’s grace and mercy that delivered him from despair and hopelessness. God’s favor covers Raymond’s life and carries him from day to day. It is written that “without me (Christ) ye can do nothing” (John 15:5). This scripture resonates in Raymond’s heart. For, he truly believes that God is the author and he is just the vessel used of God. His desire is that each poem will be taken personally and become a tool used by everyone to help them on their Christian journey and to let them know that they are never alone in their experience and quest to be closer to the Lord Jesus Christ.</p>
      <div class="author-portrait" role="img" aria-label="Portrait photograph of the author"></div>
    </section>

    <section class="front-cover">
      <div class="front-cover__cross-image" role="img" aria-label="Photograph of a wooden cross against a sunburst"></div>
      <span class="title-word title-word--top">BENEATH A COPPER</span>
      <span class="title-word title-word--left">EVENING</span>
      <span class="title-word title-word--right">SKY</span>
      <span class="title-word title-word--bottom">STILL</span>
      <span class="spine-title">BENEATH A COPPER EVENING SKY STILL</span>
      <span class="spine-author">RL Moskowicz</span>
    </section>

    <p class="front-cover__tagline">A compilation of poems by <strong>RL Moskowicz</strong></p>
  </main>
</body>
</html>
```